Business card for utility of the future

I need a business card template designed for brookvane. We provide sustainable water, energy and waste services to homes.

The card should include name, position, email address, phone number, website and our logo (attached). I would like it to convey professionalism and creativity.

Target Market(s)

Homeowners, investors, corporate partners.

Industry/Entity Type

Utility

Contact Information for Business Card

The card should include name, position, email address, phone number, website and our logo (attached).

```html
<!DOCTYPE html>
<html lang="en">
<head>
<meta charset="utf-8">
<title>brookvane business card</title>
<link href="https://fonts.googleapis.com/css2?family=Source+Sans+3:wght@400;600&display=swap" rel="stylesheet">
<style>
  :root {
    --page-bg: #e4e0de;
    --card-bg: #f3f1f0;
    --brand-green: #6cc283;
    --brand-coral: #f08a66;
    --name-ink: #5b5b5b;
    --text-light: #ffffff;
  }
  html, body {
    margin: 0;
    padding: 0;
    width: 1200px;
    height: 900px;
    overflow: hidden;
    background: var(--page-bg);
    font-family: "Source Sans 3", "Myriad Pro", Arial, sans-serif;
  }
  .business-card {
    position: absolute;
    left: 120px;
    top: 153px;
    width: 960px;
    height: 594px;
    background: var(--card-bg);
    box-shadow: 0 10px 30px rgba(0,0,0,0.12);
  }
  .brand {
    position: absolute;
    top: 0;
    left: 0;
    width: 100%;
    height: 329px;
    display: flex;
    align-items: center;
    justify-content: center;
  }
  .brand-name {
    font-weight: 600;
    font-size: 120px;
    letter-spacing: -1px;
    color: var(--name-ink);
    line-height: 1;
    margin-top: 10px;
  }
  .side-bar {
    position: absolute;
    top: 329px;
    width: 54px;
    height: 265px;
    background: var(--brand-green);
  }
  .side-bar.left { left: 0; }
  .side-bar.right { right: 0; }
  .contact-panel {
    position: absolute;
    top: 329px;
    left: 77px;
    width: 806px;
    height: 265px;
    background: var(--brand-coral);
    color: var(--text-light);
  }
  .person {
    position: absolute;
    right: 471px;
    top: 106px;
    text-align: right;
  }
  .person-name {
    font-weight: 600;
    font-size: 31px;
    line-height: 1.15;
  }
  .person-role {
    font-weight: 400;
    font-size: 29px;
    line-height: 1.15;
  }
  .contact-list {
    position: absolute;
    left: 367px;
    top: 86px;
    margin: 0;
    padding: 0;
    list-style: none;
    font-size: 25px;
    line-height: 35px;
  }
  .contact-list li {
    display: flex;
    align-items: center;
    gap: 14px;
    white-space: nowrap;
  }
  .contact-list svg {
    width: 18px;
    height: 18px;
    fill: var(--text-light);
    flex: none;
  }
</style>
</head>
<body>
  <div class="business-card">
    <div class="brand">
      <span class="brand-name">brookvane</span>
    </div>
    <div class="side-bar left"></div>
    <div class="contact-panel">
      <div class="person">
        <div class="person-name">Daniel Hartley</div>
        <div class="person-role">Position</div>
      </div>
      <ul class="contact-list">
        <li>
          <svg viewBox="0 0 24 24" aria-hidden="true"><path d="M6.6 10.8a15.1 15.1 0 0 0 6.6 6.6l2.2-2.2a1 1 0 0 1 1-.25 11.4 11.4 0 0 0 3.6.57 1 1 0 0 1 1 1V20a1 1 0 0 1-1 1A17 17 0 0 1 3 4a1 1 0 0 1 1-1h3.5a1 1 0 0 1 1 1c0 1.25.2 2.45.57 3.57a1 1 0 0 1-.25 1z"/></svg>
          021-555 730 418
        </li>
        <li>
          <svg viewBox="0 0 24 24" aria-hidden="true"><path d="M2 5h20l-10 6.5z"/><path d="M2 7l10 6.5L22 7v12H2z"/></svg>
          hello@brookvane.com
        </li>
        <li>
          <svg viewBox="0 0 24 24" aria-hidden="true"><circle cx="12" cy="12" r="10"/><path d="M2 12h20M12 2c3 3 3 17 0 20M12 2c-3 3-3 17 0 20" fill="none" stroke="#f08a66" stroke-width="1.6"/></svg>
          www.brookvane.com
        </li>
      </ul>
    </div>
    <div class="side-bar right"></div>
  </div>
</body>
</html>
```